A Real Estate Company Needs a Business Card Design

We need a business card design for a new company based in Boston MA called "Brackenfield Real Estate LLC" we are a small company but we like a big corporate look, a simple, sleek, modern and progressive look. we would like the option of having a design that could include the real estate agents personal photo and also a design if the realtor decides not to have a photo. we do not have LOGO at this moment, please use any property look pic corporate with word" Brackenfield Real Estate LLC" please see attached file as an example.
Industry/Entity Type
Business

```html
<!DOCTYPE html>
<html lang="en">
<head>
<meta charset="utf-8">
<title>Brackenfield Real Estate LLC — Business Card</title>
<link rel="stylesheet" href="https://fonts.googleapis.com/css2?family=Open+Sans:wght@400;600;700&display=swap">
<style>
  :root {
    --stage: #e9e6e1;
    --card-white: #ffffff;
    --card-white-shade: #e6e6e6;
    --card-black: #1c1c1c;
    --card-black-light: #3a3a3a;
    --band-dark: #2b2b2b;
    --band-mid: #6a6a6a;
    --ink: #3c3c3c;
    --ink-soft: #555555;
    --accent: #d81b6a;
    --white: #ffffff;
  }
  * { box-sizing: border-box; margin: 0; padding: 0; }
  html, body { width: 1200px; height: 600px; overflow: hidden; }
  body {
    background: var(--stage);
    font-family: "Open Sans", Arial, sans-serif;
    position: relative;
  }
  .card {
    position: absolute;
    top: 157px;
    width: 500px;
    height: 286px;
    border-radius: 3px;
    overflow: hidden;
    box-shadow: 0 6px 18px rgba(0,0,0,0.18);
  }
  .card--front {
    left: 60px;
    background: linear-gradient(135deg, var(--card-white) 0%, var(--card-white) 45%, var(--card-white-shade) 100%);
  }
  .card--back {
    left: 640px;
    background: linear-gradient(135deg, var(--card-black-light) 0%, var(--card-black) 55%, #111 100%);
  }
  .card__band { position: absolute; inset: 0; width: 100%; height: 100%; }

  .brand {
    position: absolute;
    display: flex;
    align-items: center;
    gap: 10px;
  }
  .brand__mark { width: 14px; height: 14px; background: var(--accent); flex: none; }
  .brand__name {
    font-weight: 600;
    text-transform: uppercase;
    line-height: 1.15;
    letter-spacing: 0.5px;
  }
  .card--front .brand { left: 34px; top: 58px; }
  .card--front .brand__name { font-size: 19px; color: var(--ink); }

  .card--back .brand { left: 50%; top: 50%; transform: translate(-50%, -50%); }
  .card--back .brand__mark { background: var(--white); width: 18px; height: 18px; }
  .card--back .brand__name { font-size: 24px; color: var(--white); }

  .contacts {
    position: absolute;
    left: 34px;
    top: 138px;
    list-style: none;
    font-size: 11.5px;
    color: var(--ink-soft);
    line-height: 1;
  }
  .contacts li { display: flex; align-items: center; gap: 8px; margin-bottom: 6px; }
  .contacts svg { width: 11px; height: 11px; flex: none; }
  .contacts .address { margin-top: 10px; display: block; line-height: 1.4; padding-left: 19px; }

  .person {
    position: absolute;
    right: 22px;
    top: 26px;
    text-align: right;
  }
  .person__name { font-size: 15px; font-weight: 700; color: var(--accent); }
  .person__role { font-size: 11px; font-weight: 600; color: var(--ink); margin-top: 2px; }
</style>
</head>
<body>

  <section class="card card--front" aria-label="Business card front">
    <svg class="card__band" viewBox="0 0 500 286" preserveAspectRatio="none" aria-hidden="true">
      <polygon points="500,96 500,110 362,144 362,286 346,286 346,132" fill="var(--band-mid)"/>
      <polygon points="500,110 500,124 378,152 378,286 362,286 362,144" fill="var(--band-dark)"/>
    </svg>

    <div class="brand">
      <span class="brand__mark"></span>
      <span class="brand__name">Brackenfield<br>Real Estate LLC</span>
    </div>

    <ul class="contacts">
      <li>
        <svg viewBox="0 0 12 12" aria-hidden="true"><rect width="12" height="12" rx="2" fill="var(--accent)"/><path d="M3.5 3h1.5l.6 1.6-.8.6a4 4 0 0 0 2 2l.6-.8 1.6.6V8.5A.8.8 0 0 1 8 9.3 5.6 5.6 0 0 1 2.7 4 .8.8 0 0 1 3.5 3z" fill="var(--white)"/></svg>
        +617 555 0142
      </li>
      <li>
        <svg viewBox="0 0 12 12" aria-hidden="true"><rect width="12" height="12" rx="2" fill="var(--accent)"/><rect x="4" y="2.5" width="4" height="7" rx=".8" fill="none" stroke="var(--white)" stroke-width="1"/></svg>
        617 555 0187
      </li>
      <li>
        <svg viewBox="0 0 12 12" aria-hidden="true"><rect width="12" height="12" rx="2" fill="var(--accent)"/><rect x="2.5" y="3.5" width="7" height="5" fill="none" stroke="var(--white)" stroke-width="1"/><path d="M2.5 3.5 6 6.5l3.5-3" fill="none" stroke="var(--white)" stroke-width="1"/></svg>
        info@brackenfield.com
      </li>
      <li>
        <svg viewBox="0 0 12 12" aria-hidden="true"><rect width="12" height="12" rx="2" fill="var(--accent)"/><circle cx="6" cy="6" r="3.3" fill="none" stroke="var(--white)" stroke-width="1"/><path d="M2.7 6h6.6M6 2.7v6.6" stroke="var(--white)" stroke-width=".8"/></svg>
        www.brackenfield.com
      </li>
      <li class="address">Here your company or<br>home address</li>
    </ul>

    <div class="person">
      <p class="person__name">Marla Quince</p>
      <p class="person__role">Founder &amp; CEO</p>
    </div>
  </section>

  <section class="card card--back" aria-label="Business card back">
    <div class="brand">
      <span class="brand__mark"></span>
      <span class="brand__name">Brackenfield<br>Real Estate LLC</span>
    </div>
  </section>

</body>
</html>
```